CD Cover (2 Sided Front & Single Sided Back) for Velmoran Band

We compose electronic music with elements from the 80s and the 90s and we are ready to release our first album. We need a simple and elegant design for our covers that matches our music. You can listen to most of the tracks here: http://tunecrate.example/velmoran . We have an existing logo that we would like to use. You can find the tracklist and the logo in the attachments. The title of the album is "Velmoran - LP".

Industry/Entity Type

Electronic

```html
<!DOCTYPE html>
<html lang="en">
<head>
<meta charset="utf-8">
<title>Velmoran - LP</title>
<link rel="stylesheet" href="https://fonts.googleapis.com/css2?family=Questrial&display=swap">
<style>
  :root {
    --night: #0a0918;
    --night-deep: #07060f;
    --dusk-peach: #f6d398;
    --dusk-gold: #e9b67c;
    --dusk-rose: #b9808f;
    --dusk-violet: #5a3a62;
    --dusk-teal: #7fd0bf;
    --logo-teal: #1d7d88;
    --label-white: #f2f2f2;
  }
  html, body {
    margin: 0;
    padding: 0;
    width: 1200px;
    height: 1200px;
    overflow: hidden;
    background: var(--night);
  }
  .cover {
    position: relative;
    width: 1200px;
    height: 1200px;
    overflow: hidden;
    background: var(--night-deep);
    font-family: "Questrial", sans-serif;
  }
  .cover-photo {
    position: absolute;
    inset: 0;
    background:
      linear-gradient(180deg, rgba(10,9,24,0) 0%, rgba(10,9,24,0) 58%, rgba(10,9,24,0.85) 72%, var(--night) 82%, var(--night-deep) 100%),
      radial-gradient(ellipse 220px 160px at 120px 520px, rgba(127,208,191,0.85), rgba(127,208,191,0) 100%),
      radial-gradient(ellipse 300px 120px at 460px 300px, rgba(185,128,143,0.8), rgba(185,128,143,0) 100%),
      radial-gradient(ellipse 420px 200px at 900px 520px, rgba(246,211,152,0.95), rgba(246,211,152,0) 100%),
      linear-gradient(172deg, rgba(60,30,60,0.75) 0%, rgba(90,58,98,0.6) 18%, rgba(90,58,98,0) 32%),
      linear-gradient(90deg, var(--dusk-violet) 0%, var(--dusk-rose) 40%, var(--dusk-gold) 75%, var(--dusk-peach) 100%);
  }
  .cover-title {
    position: absolute;
    left: 0;
    right: 0;
    top: 975px;
    display: flex;
    justify-content: center;
    align-items: flex-start;
    gap: 22px;
    padding-right: 30px;
  }
  .band-name {
    margin: 0;
    font-weight: 400;
    font-size: 86px;
    line-height: 1;
    letter-spacing: 2px;
    color: var(--logo-teal);
  }
  .release-type {
    margin-top: 30px;
    font-size: 34px;
    line-height: 1;
    color: var(--label-white);
  }
</style>
</head>
<body>
  <main class="cover">
    <div class="cover-photo" role="img" aria-label="Photograph of sheer mesh netting drifting against a warm sunset sky, tinted peach, violet and teal, fading into dark night"></div>
    <div class="cover-title">
      <h1 class="band-name">VELMORAN</h1>
      <span class="release-type">LP</span>
    </div>
  </main>
</body>
</html>
```